Oil and Gas Letterhead Design Tweak

Simple letterhead information and design tweak.

Please note, we don't want to change the design or logo of the letterhead only the small changes mentioned below.

We need to change the company name up top to "Northvale Petrotech Kestra"

Also, we need to include in the footer the following information. I have attached an image of roughly how we would like to have it displayed in the footer.

Footer Details:

Northvale Petrotech Kestra,
Unit No. 7283, Kestra Business Center, level No. 2, R&P 8, Dubai, United Arab Emirates
Northvale Petrotech Kestra is registered as a free zone company under the rules & regulations of Kestra

Target Market(s)

O&G Market

Industry/Entity Type

Oil And Gas

Font styles to use
Sans Serif

Colors

Designer to choose colors to be used in the design.

Requirements
Must have
• Change the company name to Northvale Petrotech Kestra
• Include the footer on the bottom of the first and continuation page
Should not have
• Should not change the design or logo of the letterhead, only the specified changes mentioned above

```html
<!DOCTYPE html>
<html lang="en">
<head>
<meta charset="utf-8">
<title>Northvale Petrotech Kestra – Letterhead</title>
<link rel="stylesheet" href="https://fonts.googleapis.com/css2?family=Lexend:wght@600;700&family=Carlito&display=swap">
<style>
  :root {
    --brand-blue: #0a3dff;
    --brand-red: #f00000;
    --ink: #0b0b0b;
    --paper: #ffffff;
  }
  * { margin: 0; padding: 0; box-sizing: border-box; }
  html, body { width: 849px; height: 1200px; overflow: hidden; background: var(--paper); }
  .letterhead { position: relative; width: 849px; height: 1200px; background: var(--paper); overflow: hidden; }
  .edge-bands { position: absolute; left: 0; width: 849px; }
  .edge-bands--top { top: 0; height: 16px; }
  .edge-bands--bottom { bottom: 0; height: 16px; }
  .band-blue { fill: var(--brand-blue); }
  .band-red { fill: var(--brand-red); }

  .brand { position: absolute; left: 228px; top: 44px; display: flex; align-items: center; gap: 12px; }
  .brand__mark { width: 26px; height: 26px; background: var(--brand-blue); }
  .brand__name {
    font-family: "Lexend", sans-serif; font-weight: 700; font-size: 27px;
    letter-spacing: -0.3px; color: var(--ink); text-transform: uppercase; white-space: nowrap;
  }

  .footer { position: absolute; left: 0; top: 0; width: 849px; height: 1200px; pointer-events: none; }
  .footer__company {
    position: absolute; left: 44px; top: 1095px;
    font-family: "Lexend", sans-serif; font-weight: 600; font-size: 14.5px;
    letter-spacing: -0.3px; color: var(--ink); text-transform: uppercase;
  }
  .footer__address, .footer__legal {
    font-family: "Carlito", sans-serif; color: var(--ink);
  }
  .footer__address { position: absolute; top: 1126px; left: 0; width: 849px; height: 20px; font-size: 16.5px; }
  .footer__address span { position: absolute; top: 0; white-space: nowrap; }
  .footer__address .sep { font-size: 15px; top: 2px; }
  .footer__legal { position: absolute; left: 44px; top: 1163px; font-size: 16px; white-space: nowrap; }
</style>
</head>
<body>
<main class="letterhead">
  <svg class="edge-bands edge-bands--top" viewBox="0 0 849 16" aria-hidden="true">
    <polygon class="band-blue" points="0,0 196,0 188,16 0,16"/>
    <polygon class="band-red" points="264,0 849,0 849,16 271,16"/>
  </svg>

  <header class="brand">
    <div class="brand__mark"></div>
    <h1 class="brand__name">Northvale Petrotech Kestra</h1>
  </header>

  <footer class="footer">
    <p class="footer__company">Northvale Petrotech Kestra</p>
    <p class="footer__address">
      <span style="left:44px">Unit No. 7283</span>
      <span class="sep" style="left:164px">|</span>
      <span style="left:195px">Kestra Business Center</span>
      <span class="sep" style="left:369px">|</span>
      <span style="left:396px">level No. 2, R&amp;P 8</span>
      <span class="sep" style="left:531px">|</span>
      <span style="left:554px">Dubai</span>
      <span class="sep" style="left:614px">|</span>
      <span style="left:640px">United Arab Emirates</span>
    </p>
    <p class="footer__legal">Northvale Petrotech Kestra is registered as a Free Zone Company under the Rules &amp; Regulations of Kestra</p>
  </footer>

  <svg class="edge-bands edge-bands--bottom" viewBox="0 0 849 16" aria-hidden="true">
    <polygon class="band-blue" points="624,1 660,1 652,16 616,16"/>
    <polygon class="band-red" points="668,1 695,1 703,16 660,16"/>
  </svg>
</main>
</body>
</html>
```